Heron Yards LLC - Door Hanger for Residential Mowing

Door Hanger- Heron Yards LLC. I would like the Heron Logo on a white background with three shades of pink incorporated into the flyer. Our phone number is 352-408-7716. And our website is heronyardcare.net. I would like for the door hanger to mirror the Copperfield Door Hanger, using the Heron logo & information.

List of Services to include:
Pest Control
Termite Inspection
Lawn Maintenance
Debris Clean-up
Trash Removal
Home Inspection
Handy-man Services

Target Market(s)

Residential Lawns

Industry/Entity Type

Lawn Care

Font styles to use
Sans Serif

Colors
e34197
e667a6
eea4c8
f9d9e8

Requirements
Must have
• Phone Number
• Must be a Door Hanger
• Website
• 2 Sided
Nice to have
• 3 Shades of Pink with white background
Should not have
• It must be a door hanger. KEEP IN MIND THERE WILL BE A PUNCH HOLE AT TOP.......

```html
<!DOCTYPE html>
<html lang="en">
<head>
<meta charset="utf-8">
<title>Heron Yards LLC – Door Hanger</title>
<link href="https://fonts.googleapis.com/css2?family=Lato:wght@400;700;900&display=swap" rel="stylesheet">
<style>
  :root {
    --pink-deep: #e34197;
    --pink-mid: #e667a6;
    --pink-soft: #eea4c8;
    --pink-pale: #f9d9e8;
    --white: #ffffff;
    --ink: #3a3a3a;
    --stage: #efeae6;
    --grass-dark: #3f9a1e;
    --grass-light: #8fd34a;
  }
  * { box-sizing: border-box; margin: 0; padding: 0; }
  html, body { width: 1200px; height: 960px; overflow: hidden; }
  body {
    background: var(--stage);
    font-family: "Lato", sans-serif;
    position: relative;
  }
  .hanger {
    position: absolute;
    top: 55px;
    width: 330px;
    height: 850px;
    background: var(--white);
    overflow: hidden;
    box-shadow: 0 4px 14px rgba(0,0,0,0.18);
  }
  .hanger--front { left: 230px; }
  .hanger--back { left: 640px; }
  .drape { position: absolute; inset: 0; width: 100%; height: 100%; }
  .punch-hole {
    position: absolute;
    left: 119px; top: 53px;
    width: 92px; height: 92px;
    border-radius: 50%;
    background: var(--stage);
  }
  .brand-mark {
    position: absolute;
    border-radius: 50%;
    background: var(--pink-deep);
  }
  .front-mark { left: 135px; top: 226px; width: 60px; height: 60px; }
  .back-mark { left: 40px; top: 232px; width: 22px; height: 22px; }
  .brand-name {
    position: absolute;
    color: var(--pink-deep);
    font-weight: 400;
    white-space: nowrap;
  }
  .front-name { left: 0; width: 100%; text-align: center; top: 372px; font-size: 28px; }
  .back-name { left: 76px; top: 228px; font-size: 25px; }
  .headline {
    position: absolute; top: 484px; width: 100%;
    text-align: center; color: var(--ink);
    font-weight: 700; font-size: 20px; line-height: 27px; letter-spacing: -0.3px;
  }
  .price-box {
    position: absolute; left: 44px; top: 515px;
    width: 237px; height: 62px;
    border: 1.5px solid var(--pink-deep);
    border-radius: 31px;
    background: var(--white);
  }
  .price-box .currency {
    position: absolute; left: 18px; top: 10px;
    color: var(--pink-deep); font-weight: 900; font-size: 28px;
  }
  .price-box .unit {
    position: absolute; right: 26px; top: 38px;
    font-size: 12px; font-weight: 700; color: var(--ink);
  }
  .fine-print {
    position: absolute; top: 619px; width: 100%; text-align: center;
    font-size: 14.5px; font-weight: 700; color: var(--ink); letter-spacing: -0.2px;
  }
  .call-line {
    position: absolute; top: 656px; width: 100%; text-align: center;
    font-size: 22px; color: var(--ink);
  }
  .base-band {
    position: absolute; left: 0; top: 744px; width: 100%; height: 106px; background: var(--white);
  }
  .phone {
    position: absolute; left: 18px; top: 709px;
    width: 292px; height: 48px;
    background: var(--pink-deep);
    color: var(--white);
    font-weight: 900; font-size: 34px; letter-spacing: 3.5px;
    text-align: center; line-height: 48px;
  }
  .website {
    position: absolute; top: 767px; width: 100%; text-align: center;
    font-size: 21px; color: var(--pink-deep);
  }
  .grass {
    position: absolute; left: 0; bottom: 0; width: 100%; height: 50px;
    background: linear-gradient(180deg, var(--grass-light) 0%, var(--grass-dark) 100%);
  }
  .services-title {
    position: absolute; top: 302px; left: 64px;
    font-size: 22px; font-weight: 700; color: var(--pink-deep);
  }
  .services {
    position: absolute; top: 342px; left: 80px; list-style: none;
  }
  .services li {
    position: relative; padding-left: 26px;
    font-size: 18.5px; line-height: 31.3px; color: var(--ink);
  }
  .services li::before {
    content: ""; position: absolute; left: 0; top: 12px;
    width: 8px; height: 8px; border-radius: 50%; background: var(--pink-mid);
  }
</style>
</head>
<body>

<svg width="0" height="0" style="position:absolute">
  <defs>
    <linearGradient id="drape-top" x1="0" y1="0" x2="0" y2="1">
      <stop offset="0" stop-color="#e667a6"/>
      <stop offset="1" stop-color="#f9d9e8" stop-opacity="0"/>
    </linearGradient>
    <linearGradient id="drape-low" x1="0" y1="0" x2="0" y2="1">
      <stop offset="0" stop-color="#ffffff" stop-opacity="0"/>
      <stop offset="0.55" stop-color="#f9d9e8"/>
      <stop offset="1" stop-color="#eea4c8"/>
    </linearGradient>
    <linearGradient id="drape-side" x1="0" y1="0" x2="0" y2="1">
      <stop offset="0" stop-color="#e34197" stop-opacity="0"/>
      <stop offset="1" stop-color="#e667a6"/>
    </linearGradient>
  </defs>
</svg>

<section class="hanger hanger--front">
  <svg class="drape" viewBox="0 0 330 850" preserveAspectRatio="none" aria-hidden="true">
    <rect x="0" y="0" width="330" height="200" fill="url(#drape-top)" opacity="0.45"/>
    <path d="M0 0 H55 Q40 120 0 230 Z" fill="url(#drape-top)"/>
    <path d="M330 0 H270 Q290 120 330 230 Z" fill="url(#drape-top)"/>
    <path d="M95 0 H235 L165 70 Z" fill="#e667a6" opacity="0.7"/>
    <rect x="0" y="450" width="330" height="300" fill="url(#drape-low)"/>
    <path d="M0 540 Q60 600 70 750 H0 Z" fill="url(#drape-side)"/>
    <path d="M330 540 Q270 600 260 750 H330 Z" fill="url(#drape-side)"/>
  </svg>
  <div class="punch-hole"></div>
  <div class="brand-mark front-mark"></div>
  <h1 class="brand-name front-name">Heron Yards LLC</h1>
  <p class="headline">Now offering Lawn Mowing<br>In Your Neighborhood</p>
  <div class="price-box"><span class="currency">$</span><span class="unit">per service</span></div>
  <p class="fine-print">No binding contract required</p>
  <p class="call-line">Call to schedule service today</p>
  <div class="base-band"></div>
  <div class="phone">352-408-7716</div>
  <p class="website">heronyardcare.net</p>
  <div class="grass" role="img" aria-label="Strip of green grass along the bottom edge"></div>
</section>

<section class="hanger hanger--back">
  <svg class="drape" viewBox="0 0 330 850" preserveAspectRatio="none" aria-hidden="true">
    <rect x="0" y="0" width="330" height="200" fill="url(#drape-top)" opacity="0.45"/>
    <path d="M0 0 H55 Q40 120 0 230 Z" fill="url(#drape-top)"/>
    <path d="M330 0 H270 Q290 120 330 230 Z" fill="url(#drape-top)"/>
    <path d="M95 0 H235 L165 70 Z" fill="#e667a6" opacity="0.7"/>
    <rect x="0" y="450" width="330" height="300" fill="url(#drape-low)"/>
    <path d="M0 540 Q60 600 70 750 H0 Z" fill="url(#drape-side)"/>
    <path d="M330 540 Q270 600 260 750 H330 Z" fill="url(#drape-side)"/>
  </svg>
  <div class="punch-hole"></div>
  <div class="brand-mark back-mark"></div>
  <h2 class="brand-name back-name">Heron Yards LLC</h2>
  <h3 class="services-title">Services Available:</h3>
  <ul class="services">
    <li>Pest Control</li>
    <li>Termite Inspection</li>
    <li>Lawn Maintenance</li>
    <li>Debris Clean-up</li>
    <li>Trash Removal</li>
    <li>Home Inspection</li>
    <li>Handy-man Services</li>
  </ul>
  <p class="call-line">Call today for a free estimate</p>
  <div class="base-band"></div>
  <div class="phone">352-408-7716</div>
  <p class="website">heronyardcare.net</p>
  <div class="grass" role="img" aria-label="Strip of green grass along the bottom edge"></div>
</section>

</body>
</html>
```